Task Description:
I’m wanting a professionally designed 8 ½' x 11, 3 fold brochure, both sides, to print as my target audience are those people who primarily don’t have access to the internet. These items will be dropped off in the mailboxes of all households in the city.
However I do have a web site www.brightcivicpath.ca where I would like to have it as a document that can be down loaded.
This is my first foray into political office and my message needs to be clear, concise and easy to understand. The brochure should be a bit conservative yet be warm and inviting. I’ve selected two pictures that I think make sense under their respective headings, but I'm open to suggestions.I need to update my picture for the front cover.
There is the possibility of having T shirts and business cards made up, which would be in essence a simpler version of the brochure so please keep this in mind. I ask that you work with me and I will compensate you accordingly for the extras should they be required. You may want to consider making the Bright Civic Path into a logo as we own all the web extensions and have applied for copyright protection for branding purposes.
You may want to look at QM Larchfield http://www.qmlarchfield.ca/ , or the Pinecrest Bank of Canada www.pinecrestbank.com as two recognizable colour schemes here in Canada but don’t let that limit your imagination.
The content in the flier should remain intact although I am open to some minor suggestions. As you can see my talents as a graphic artist are limited hence my need for that professional make over that will give it a bit of razzle dazzle and set me out from the other candidates. So use your imagination!!
Target Market(s)
Middle age voters who may or may not have access to the internet and still prefer print
Industry/Entity Type
Conservative

```html
<!DOCTYPE html>
<html lang="en">
<head>
<meta charset="utf-8">
<title>Bright Civic Path – Brochure Inside Spread</title>
<link rel="stylesheet" href="https://fonts.googleapis.com/css2?family=Oswald:wght@500;600&family=Open+Sans:wght@400&family=Ubuntu:wght@500;700&display=swap">
<style>
  :root {
    --maroon: #5e0f0f;
    --maroon-deep: #3d0606;
    --maroon-mid: #7a1a18;
    --paper: #c9c3b9;
    --ink: #2d2622;
    --heading-dark: #2a1a14;
    --quote-grey: #9a948c;
    --url-light: #d9d3cb;
  }
  * { margin: 0; padding: 0; box-sizing: border-box; }
  html, body { width: 1200px; height: 848px; overflow: hidden; background: var(--paper); }
  .spread { position: relative; width: 1200px; height: 848px; background: var(--paper); overflow: hidden; }
  .top-bar { position: absolute; left: 0; top: 0; width: 1200px; height: 30px;
    background: linear-gradient(var(--maroon-deep), var(--maroon)); }
  .top-bar::after { content: ""; position: absolute; left: 0; right: 0; top: 20px; height: 1px; background: #a5605a; }
  .header-art { position: absolute; left: 0; top: 28px; }

  .column { position: absolute; font-family: "Open Sans", sans-serif; font-size: 12.4px;
    line-height: 18px; color: var(--ink); }
  .column p { margin-bottom: 18px; }
  .column.justified p { text-align: justify; }
  .col-economy { left: 41px; top: 305px; width: 337px; }
  .col-opportunity { left: 436px; top: 240px; width: 335px; }
  .col-safety { left: 832px; top: 192px; width: 330px; }
  .col-opportunity p, .col-safety p { margin-bottom: 14px; }

  .section-title { font-family: "Oswald", sans-serif; font-weight: 600; font-size: 39px;
    letter-spacing: -1.5px; color: #fff; line-height: 1; white-space: nowrap;
    text-shadow: 1px 1px 2px rgba(0,0,0,.35); margin-bottom: 22px; }
  .section-title .quote { color: var(--quote-grey); font-size: 34px; vertical-align: top; }
  .sub-title { font-family: "Ubuntu", sans-serif; font-weight: 700; font-size: 27px;
    color: var(--heading-dark); margin: 6px 0 16px; letter-spacing: -.3px; }
  .closing-line { font-family: "Ubuntu", sans-serif; font-weight: 500; font-size: 16px;
    color: var(--heading-dark); letter-spacing: -.2px; }
  .col-economy .closing-line { margin-top: 6px; }
  .col-opportunity .closing-line { margin-top: 24px; }
  .brand-inline { font-family: "Ubuntu", sans-serif; font-weight: 700; font-size: 15px; color: var(--heading-dark); }

  .photo-slot { width: 329px; height: 149px; margin: 2px 0 8px;
    background: linear-gradient(90deg, #2e2a27, #6d5f55 45%, #a39c94); position: relative;
    border: 1px solid #5b524b; }
  .photo-caption { position: absolute; left: 4px; bottom: 2px; font-size: 9.5px; color: #fff;
    background: rgba(0,0,0,.55); padding: 0 4px; line-height: 13px; }

  .footer-bar { position: absolute; left: 0; top: 798px; width: 1200px; height: 50px;
    background: linear-gradient(var(--maroon-mid), var(--maroon-deep)); }
  .footer-bar::before { content: ""; position: absolute; left: 0; right: 0; top: 2px; height: 1px; background: #a5605a; }
  .footer-url { position: absolute; top: 10px; font-family: "Ubuntu", sans-serif; font-weight: 500;
    font-size: 20px; color: var(--url-light); letter-spacing: -.3px; }
</style>
</head>
<body>
<main class="spread">
  <div class="top-bar"></div>

  <svg class="header-art" width="1200" height="290" viewBox="0 0 1200 290" aria-hidden="false">
    <defs>
      <clipPath id="strip-clip">
        <path d="M0,0 H1200 V108 C800,118 400,150 0,242 Z"/>
      </clipPath>
      <linearGradient id="band" x1="0" y1="0" x2="0" y2="1">
        <stop offset="0" stop-color="#7a1a18"/>
        <stop offset="1" stop-color="#3d0606"/>
      </linearGradient>
    </defs>
    <g clip-path="url(#strip-clip)">
      <rect x="0" y="0" width="340" height="260" fill="#8a6b52" role="img" aria-label="Photo of a historic red brick building with a turret under blue sky"/>
      <rect x="340" y="0" width="257" height="260" fill="#7e93a6" role="img" aria-label="Photo of modern building columns against a blue sky"/>
      <rect x="599" y="0" width="197" height="260" fill="#8a98a4" role="img" aria-label="Photo of sailboats moored at a marina"/>
      <rect x="798" y="0" width="159" height="260" fill="#8c5a4e" role="img" aria-label="Photo of a baseball stadium grandstand"/>
      <rect x="959" y="0" width="130" height="260" fill="#6f97b8" role="img" aria-label="Photo of a bird diving over calm water"/>
      <rect x="1091" y="0" width="109" height="260" fill="#4a4a48" role="img" aria-label="Photo of a sunset over a harbour bridge"/>
    </g>
    <path d="M0,242 C400,150 800,118 1200,108 V138 C800,148 400,180 0,278 Z" fill="url(#band)"/>
    <path d="M0,242 C400,150 800,118 1200,108" fill="none" stroke="#b0736b" stroke-width="1.2"/>
  </svg>

  <section class="column col-economy">
    <h2 class="section-title"><span class="quote">“</span>A Strong Economy<span class="quote">”</span></h2>
    <p>Without a strong economy we can’t afford to pay for social services that we now take for granted.</p>
    <p>Although the City is the largest corporation it is unique in the fact that it revenue stream is tied directly to taxation.</p>
    <p>Without new business and new citizens the burden of taxes will fall increasingly on residential taxpayers.</p>
    <p>Our demographics have changed over the years and those changes need to be reflected in the way we tax our citizens.</p>
    <p>Our levels of debts and our future commitments need to be effectively communicated to the people that own this city. You the tax payer!!</p>
    <p>Currently our city debt is 178 million dollars with further commitments of 153 million for homes for the aged, under-funded capital projects and the possibility of 100 million dollar multi purpose facility.</p>
    <h3 class="closing-line">How will we pay for this?</h3>
  </section>

  <section class="column col-opportunity justified">
    <h2 class="section-title"><span class="quote">“</span>New Opportunities<span class="quote">”</span></h2>
    <h3 class="sub-title">New Beginnings</h3>
    <p>As a city we need to rekindle that passion that made us the most modern small city in North America at the turn of the century.</p>
    <p>That means, if you currently own and operate a business large or small we need your input to improve the efficiency of how we deliver services. No more endless meetings without any results.</p>
    <p>If you’re in the planning stages and need assistance, the city will be there to offer support and guidance.</p>
    <p>Regional projects such as the proposed Cedar Hollow Iron Mine in Millbrook, or the restart of Stonecliff Pulp are vitality important to the flow of goods and services in the city and surrounding communities.</p>
    <p>As <span class="brand-inline">Bright Civic Path</span> I have personally spoken to the CEO’s of several new industries that have never even considered Harbour Ridge before they received my call. These are leading edge technologies that have the high growth potential. Jobs and opportunities for young and old alike.</p>
    <h3 class="closing-line">Are we open for business absolutely!</h3>
  </section>

  <section class="column col-safety justified">
    <h2 class="section-title"><span class="quote">“</span>A Safe Community<span class="quote">”</span></h2>
    <p>Without a safe community it will be difficult to attract new people and new businesses to our community.</p>
    <p>Consultation with our citizens and direct input from all members of the police force is essential so that we can maximize our resources and deliver the best possible results to those people directly affected by criminal activity.</p>
    <p>Incentive programs need to be encouraged in all city departments at the ground level so that good ideas don’t get lost in bureaucracy. Those incentives could extend to ordinary citizens who feel good ideas go unnoticed and unrewarded. Management doesn’t have all the solutions!!</p>
    <p>Seniors, youth and women are the most vulnerable of all.. More efficient use of city resources will identify those groups and individuals with the greatest needs. Trained volunteers could assist senior home owners apply for under utilized grant programs that would allow them to stay in their homes longer as an example.</p>
    <div class="photo-slot" role="img" aria-label="Photo of the candidate's father seated in arena stands beside the team mascot">
      <span class="photo-caption">My Dad @ 92 with NRU Mascot</span>
    </div>
    <h3 class="closing-line">Protecting the most vulnerable is important!</h3>
  </section>

  <footer class="footer-bar">
    <span class="footer-url" style="left:96px">www.brightcivicpath.ca</span>
    <span class="footer-url" style="left:483px">www.brightcivicpath.ca</span>
    <span class="footer-url" style="left:888px">www.brightcivicpath.ca</span>
  </footer>
</main>
</body>
</html>
```